Video Company Business Card Design

We are looking for a new design for business cards that will complement our new logo and new website design.

Target Market(s)

professionals who need video work done

Industry/Entity Type

Business

Requirements
Must have
• Logo
compliment website look seen here...http://k7studiowerks.com/brightlens/

info for card:
Derek Halloway
Producer/ Cinematographer

462 Pendlemoor SW
Grand Rapids, MI 49504
(inside The VARN Center)
(616) 555-0174
Derek@brightlensfilms.com
www.brightlensfilms.com

```html
<!DOCTYPE html>
<html lang="en">
<head>
<meta charset="utf-8">
<title>BrightLens Films – Business Cards</title>
<link rel="stylesheet" href="https://fonts.googleapis.com/css2?family=Josefin+Sans:wght@300;400;600&display=swap">
<style>
  :root {
    --backdrop: #2b2b2b;
    --card: #ffffff;
    --band: #333333;
    --green: #2bb24c;
    --ink: #2e2e2e;
    --muted: #c9c9c9;
  }
  * { margin: 0; padding: 0; box-sizing: border-box; }
  html, body { width: 1000px; height: 1200px; overflow: hidden; background: var(--backdrop); }
  body { position: relative; font-family: "Josefin Sans", sans-serif; color: var(--ink); }

  .card { position: absolute; left: 177px; width: 644px; height: 368px; background: var(--card); overflow: hidden; }
  .card--front { top: 27px; }
  .card--back-a { top: 418px; }
  .card--back-b { top: 809px; }

  .card__band { position: absolute; left: 0; top: 333px; width: 100%; height: 18px; background: var(--band); overflow: hidden; }

  .brand { position: absolute; left: 45px; top: 150px; }
  .brand__name { font-weight: 600; font-size: 48px; color: var(--green); letter-spacing: 2.2px; line-height: 1; white-space: nowrap; }
  .brand__tagline { position: absolute; left: 46px; top: 198px; font-size: 13px; font-weight: 400; letter-spacing: 6.4px; color: var(--ink); text-transform: uppercase; white-space: nowrap; }

  .band-url { position: absolute; right: 20px; top: 3px; font-size: 11px; letter-spacing: 5px; color: var(--green); text-transform: uppercase; line-height: 14px; }

  .band-brand { position: absolute; top: 1px; font-weight: 600; font-size: 15px; color: var(--green); line-height: 16px; white-space: nowrap; }

  .person { position: absolute; left: 47px; top: 154px; }
  .person__name { font-weight: 400; font-size: 34px; line-height: 1; color: var(--ink); white-space: nowrap; }
  .person__first { color: var(--green); }
  .person__role { font-size: 18px; font-weight: 300; margin-top: 6px; color: var(--ink); white-space: nowrap; }

  .divider { position: absolute; left: 321px; top: 137px; width: 1px; height: 100px; background: linear-gradient(var(--card), var(--muted) 30%, var(--muted) 70%, var(--card)); }

  .contact { position: absolute; left: 358px; top: 148px; list-style: none; }
  .contact__row { display: flex; font-size: 19px; font-weight: 300; line-height: 25px; white-space: nowrap; }
  .contact__label { width: 32px; color: var(--green); font-size: 17px; font-weight: 300; }
  .address { position: absolute; left: 390px; top: 232px; font-size: 12px; font-weight: 300; line-height: 16.5px; color: var(--ink); font-style: normal; white-space: nowrap; }
</style>
</head>
<body>

<section class="card card--front">
  <div class="brand"><span class="brand__name">BRIGHTLENSFILMS</span></div>
  <p class="brand__tagline">Grand Rapids Based Video Production</p>
  <div class="card__band"><span class="band-url">www.brightlensfilms.com</span></div>
</section>

<section class="card card--back-a">
  <div class="person">
    <h1 class="person__name"><span class="person__first">Derek</span> Halloway</h1>
    <p class="person__role">Producer/ Cinematographer</p>
  </div>
  <div class="divider"></div>
  <ul class="contact">
    <li class="contact__row"><span class="contact__label">p:</span>(616) 555-0174</li>
    <li class="contact__row"><span class="contact__label">w:</span>www.brightlensfilms.com</li>
    <li class="contact__row"><span class="contact__label">e:</span>derek@brightlensfilms.com</li>
  </ul>
  <address class="address">462 Pendlemoor SW<br>Grand Rapids, MI 49504<br>-inside The VARN Center</address>
  <div class="card__band">
    <span class="band-brand" style="left:30px">BRIGHTLENSFILMS</span>
  </div>
</section>

<section class="card card--back-b">
  <div class="person">
    <h1 class="person__name"><span class="person__first">Derek</span> Halloway</h1>
    <p class="person__role">Producer/ Cinematographer</p>
  </div>
  <div class="divider"></div>
  <ul class="contact">
    <li class="contact__row"><span class="contact__label">p:</span>(616) 555-0174</li>
    <li class="contact__row"><span class="contact__label">w:</span>www.brightlensfilms.com</li>
    <li class="contact__row"><span class="contact__label">e:</span>derek@brightlensfilms.com</li>
  </ul>
  <address class="address">462 Pendlemoor SW<br>Grand Rapids, MI 49504<br>-inside The VARN Center</address>
  <div class="card__band">
    <span class="band-brand" style="left:8px">BRIGHTLENSFILMS</span>
    <span class="band-brand" style="left:199px">BRIGHTLENSFILMS</span>
    <span class="band-brand" style="left:391px">BRIGHTLENSFILMS</span>
    <span class="band-brand" style="left:585px">BRIGHTLENSFILMS</span>
  </div>
</section>

</body>
</html>
```